Business Card Design Project

We would need a business name card for our online website business, http://www.brindle.com.sg/. We would need to include our website on the name card as well.

Target Market(s)

Adults and kids in Singapore, mainly expatriates

Industry/Entity Type

Business

Font styles to use
Sans Serif

Colors

Designer to choose colors to be used in the design.

Requirements
Must have
• Must include our "vorn" logo and we would like our name card to be printed on light craft paper material

```html
<!DOCTYPE html>
<html lang="en">
<head>
<meta charset="utf-8">
<title>Vorn Business Card</title>
<link href="https://fonts.googleapis.com/css2?family=Open+Sans:wght@400;700&display=swap" rel="stylesheet">
<style>
  :root {
    --bg: #ece8e2;
    --paper: #ffffff;
    --ink: #1c1c1c;
    --teal: #119fb3;
    --red: #e31e3c;
    --pink: #f5aec8;
    --yellow: #ffd21a;
    --green: #0ba779;
    --blue: #0b6cb7;
    --navy: #263570;
    --badge-orange: #f26a2a;
    --badge-teal: #22b5c7;
    --badge-yellow: #fdd115;
    --badge-pink: #f082ac;
  }
  * { margin: 0; padding: 0; box-sizing: border-box; }
  html, body { width: 1200px; height: 1000px; overflow: hidden; }
  body {
    background: var(--bg);
    font-family: "Open Sans", Verdana, sans-serif;
    color: var(--ink);
    display: flex;
    flex-direction: column;
    align-items: center;
    justify-content: center;
    gap: 44px;
  }
  .card {
    width: 780px;
    height: 434px;
    position: relative;
    overflow: hidden;
    box-shadow: 0 6px 18px rgba(0,0,0,0.18);
  }

  /* Back side */
  .card-back { background: var(--paper); }
  .back-pattern {
    position: absolute;
    inset: 0;
    background: linear-gradient(120deg, var(--red) 0%, var(--yellow) 30%, var(--blue) 55%, var(--pink) 75%, var(--teal) 100%);
    opacity: 0.9;
  }
  .back-mark {
    position: absolute;
    left: 50%; top: 50%;
    width: 200px; height: 200px;
    transform: translate(-50%, -50%);
    border-radius: 50%;
    background: var(--paper);
    display: flex; align-items: center; justify-content: center;
  }
  .back-mark .brand-name {
    font-weight: 700;
    font-size: 40px;
    letter-spacing: 2px;
    color: var(--navy);
  }

  /* Front side */
  .card-front { background: var(--paper); }
  .brand-title {
    position: absolute;
    left: 36px; top: 44px;
    font-size: 40px;
    font-weight: 400;
    letter-spacing: 1px;
  }
  .brand-title sup { font-size: 16px; vertical-align: 20px; }
  .contact-list {
    position: absolute;
    left: 36px; top: 118px;
    list-style: none;
  }
  .contact-item {
    display: flex; align-items: center; gap: 10px;
    font-size: 21px;
    line-height: 32px;
  }
  .contact-item.primary { font-size: 25px; }
  .contact-icon { width: 20px; height: 20px; flex: none; }
  .icon-web { border-radius: 50%; background: var(--green); }
  .icon-social { border-radius: 3px; background: var(--blue); }
  .icon-photo { border-radius: 4px; background: var(--red); }

  .front-mark {
    position: absolute;
    right: 42px; top: 40px;
    width: 150px; height: 150px;
    border-radius: 50%;
    background: var(--navy);
    display: flex; align-items: center; justify-content: center;
  }
  .front-mark .brand-name {
    font-weight: 700;
    font-size: 30px;
    letter-spacing: 2px;
    color: var(--paper);
  }

  .stripe-bar {
    position: absolute;
    left: 0; width: 100%; height: 13px;
    background: linear-gradient(90deg, var(--red), var(--yellow) 30%, var(--green) 50%, var(--blue) 70%, var(--teal));
  }
  .stripe-top { top: 292px; }
  .stripe-bottom { top: 404px; }

  .category-row {
    position: absolute;
    left: 0; top: 312px;
    width: 100%;
    display: flex;
    justify-content: space-around;
    padding: 0 60px 0 40px;
  }
  .category-badge {
    width: 82px; height: 82px;
    border-radius: 50%;
    display: flex; align-items: center; justify-content: center;
    text-align: center;
    color: #fff;
    font-size: 9px;
    font-weight: 700;
    text-transform: uppercase;
    letter-spacing: 0.5px;
    line-height: 1.2;
    box-shadow: inset 0 0 0 6px rgba(255,255,255,0.8);
  }
  .badge-sweets { background: var(--badge-orange); }
  .badge-chocolates { background: var(--badge-teal); }
  .badge-drinks { background: var(--badge-yellow); }
  .badge-snacks { background: var(--badge-pink); }
</style>
</head>
<body>

<section class="card card-back" aria-label="Card back">
  <div class="back-pattern" role="img" aria-label="Multicolour diagonal stripe pattern"></div>
  <div class="back-mark"><span class="brand-name">VORN</span></div>
</section>

<section class="card card-front" aria-label="Card front">
  <h1 class="brand-title">VORN<sup>™</sup></h1>

  <ul class="contact-list">
    <li class="contact-item primary"><span class="contact-icon icon-web"></span>www.brindle.com.sg</li>
    <li class="contact-item"><span class="contact-icon icon-social"></span>www.kwiblrhub.com/vornsingapore</li>
    <li class="contact-item"><span class="contact-icon icon-photo"></span>vornsingapore</li>
  </ul>

  <div class="front-mark"><span class="brand-name">VORN</span></div>

  <div class="stripe-bar stripe-top" role="img" aria-label="Multicolour stripe band"></div>

  <div class="category-row">
    <div class="category-badge badge-sweets">Sweets</div>
    <div class="category-badge badge-chocolates">Chocolates</div>
    <div class="category-badge badge-drinks">Drinks</div>
    <div class="category-badge badge-snacks">Crisps<br>&amp;<br>Snacks</div>
  </div>

  <div class="stripe-bar stripe-bottom" role="img" aria-label="Multicolour stripe band"></div>
</section>

</body>
</html>
```